Business Cards for Law Office of Denise R. Harlow

I need a business card for my new estate planning law firm. I have attached my logo. I would like a design that is professional but not too formal or stuffy.

Target Market(s)

Professionals (lawyers, doctors, businesswomen) between the age of 30 and 50 who are tech-savvy and educated.

Industry/Entity Type

Lawyer

Contact Information for Business Card

Denise R. Harlow

528 E. 19th Street
7th Floor
New York, NY 10583

Phone: (855) 602-7318
Direct: (917) 463-5071
Email: Denise@DeniseRHarlowLegal.test
www.DeniseRHarlowLegal.test

Font styles to use
Other font styles liked:
• Corbel

Requirements
Must have
• On the front:
• Denise R. Harlow, Esq.
• Owner & Founder
• 528 E. 19th Street
• 7th Floor
• New York, NY 10583
• Phone: (855) 602-7318
• Direct: (917) 463-5071
• Email: denise@deniserharlowlegal.test
• www.deniserharlowlegal.test
• On the back:
• LOGO
Nice to have
• I want it to be professional but not too formal or stuffy. Please choose colors that go with my logo.
Should not have
• I don't want TOO MUCH color. Some color is good, but not too much.

```html
<!DOCTYPE html>
<html lang="en">
<head>
<meta charset="utf-8">
<title>Law Office of Denise R. Harlow — Business Cards</title>
<link href="https://fonts.googleapis.com/css2?family=Open+Sans:wght@400;600&display=swap" rel="stylesheet">
<style>
  :root {
    --page-bg: #ece9e4;
    --card-top: #f5e3db;
    --card-bottom: #ebb3a8;
    --ink: #1c1c1c;
    --brand-purple: #7b1f78;
    --rule: #2a2a2a;
  }
  * { box-sizing: border-box; margin: 0; padding: 0; }
  html, body {
    width: 1200px;
    height: 842px;
    overflow: hidden;
    background: var(--page-bg);
    font-family: "Open Sans", sans-serif;
    color: var(--ink);
  }
  .sheet {
    width: 1200px;
    height: 842px;
    display: flex;
    align-items: center;
    justify-content: center;
    gap: 56px;
  }
  .card {
    position: relative;
    width: 532px;
    height: 304px;
    background: linear-gradient(180deg, var(--card-top) 0%, var(--card-bottom) 100%);
    box-shadow: 0 2px 6px rgba(0,0,0,0.18);
  }
  /* Back: firm name */
  .card--back {
    display: flex;
    align-items: center;
    justify-content: center;
  }
  .firm-name {
    font-weight: 600;
    font-size: 30px;
    letter-spacing: 0.04em;
    text-transform: uppercase;
    color: var(--brand-purple);
    text-align: center;
    line-height: 1.25;
  }
  /* Front: contact details */
  .website {
    position: absolute;
    top: 36px;
    left: 0;
    right: 0;
    text-align: center;
    font-size: 19px;
    letter-spacing: 0.22em;
  }
  .email {
    position: absolute;
    top: 78px;
    left: 0;
    right: 0;
    text-align: center;
    font-size: 14px;
    letter-spacing: 0.02em;
  }
  .attorney {
    position: absolute;
    top: 112px;
    left: 0;
    right: 0;
    text-align: center;
  }
  .attorney__name {
    font-size: 15px;
    font-weight: 600;
    letter-spacing: 0.04em;
    color: var(--brand-purple);
    line-height: 1.4;
  }
  .attorney__title {
    font-size: 12px;
    letter-spacing: 0.06em;
    line-height: 1.4;
  }
  .address {
    position: absolute;
    left: 40px;
    bottom: 30px;
    font-size: 16px;
    line-height: 1.45;
    letter-spacing: 0.04em;
    font-style: normal;
  }
  .address::before {
    content: "";
    display: block;
    width: 56px;
    height: 1px;
    background: var(--rule);
    margin-bottom: 12px;
  }
  .phones {
    position: absolute;
    right: 40px;
    bottom: 80px;
    font-size: 14px;
    line-height: 1.55;
    letter-spacing: 0.04em;
  }
</style>
</head>
<body>
  <main class="sheet">
    <section class="card card--back" aria-label="Card back">
      <p class="firm-name">Law Office of<br>Denise R. Harlow</p>
    </section>
    <section class="card card--front" aria-label="Card front">
      <p class="website">www.DeniseRHarlowLegal.test</p>
      <p class="email">Email: Denise@DeniseRHarlowLegal.test</p>
      <div class="attorney">
        <p class="attorney__name">Denise R. Harlow, Esq.</p>
        <p class="attorney__title">Owner &amp; Founder</p>
      </div>
      <address class="address">528 E. 19th Street<br>7th Floor<br>New York, NY 10583</address>
      <p class="phones">Phone: (855) 602-7318<br>Direct: (917) 463-5071</p>
    </section>
  </main>
</body>
</html>
```